business cards, stationary, email signature
Professional
Greta Volsky
President
Corporate office:
3620 E Tamsin Road, Orange, CA 92814
Other locations in San Diego, CA and Reno, NV
greta@farwellgrp.net
www.farwellgrp.net
482650, K, D74
*8(a), *SDB, *SBE, *MBE, *DBE, *CBE
these certifications should be listed in the middle, bottom of the card.
■221119 – Other Electric Power Generation
■236210 – Industrial Building Construction
■236220 – Commercial and Institutional Building Construction
■237310 – Highway, Street, and Bridge Construction
■238160 – Roofing Contractors
■238170 – Siding Contractors
■238220 – Plumbing, Heating, and Air-Conditioning Contractors
■238310 – Drywall and Insulation Contractors
■238320 – Painting and Wall Covering Contractors
■238340 – Tile and Terrazzo Contractors
■238350 – Finish Carpentry Contractors
■238390 – Other Building Finishing Contractors
■238910 – Site Preparation Contractors
■238990 – All Other Specialty Trade Contractors
■541350 – Building Inspection Services
■561210 – Facilities Support Services
■561790 – Other Services to Buildings and Dwellings

```html
<!DOCTYPE html>
<html lang="en">
<head>
<meta charset="utf-8">
<title>Farwell Group – Business Card</title>
<link rel="stylesheet" href="https://fonts.googleapis.com/css2?family=Open+Sans:wght@400;600;700&display=swap">
<style>
  :root {
    --bg: #e9e6e1;
    --card-dark: #262a2c;
    --card-dark-2: #3b4043;
    --green: #9cc06a;
    --green-light: #d9e8b7;
    --green-pale: #eef3df;
    --green-deep: #6f9a3e;
    --orange: #f0a23a;
    --white: #ffffff;
    --ink: #2d3436;
    --ink-soft: #55605f;
  }
  * { margin: 0; padding: 0; box-sizing: border-box; }
  html, body { width: 1200px; height: 432px; overflow: hidden; }
  body {
    background: var(--bg);
    font-family: "Open Sans", Arial, sans-serif;
    position: relative;
  }
  .card {
    position: absolute;
    top: 56px;
    width: 540px;
    height: 320px;
    border-radius: 12px;
    overflow: hidden;
    box-shadow: 0 4px 14px rgba(0,0,0,.18);
  }
  /* Front */
  .card-front {
    left: 40px;
    background: linear-gradient(160deg, var(--card-dark-2), var(--card-dark) 70%);
    color: var(--white);
  }
  .front-wave { position: absolute; left: 0; bottom: 0; width: 540px; height: 160px; }
  .brand {
    position: absolute; top: 30px; left: 30px;
    display: flex; align-items: center; gap: 18px;
  }
  .brand-dot {
    width: 74px; height: 74px; border-radius: 50%;
    background: var(--orange);
  }
  .brand-name {
    font-weight: 600; font-size: 34px; letter-spacing: 3px;
    color: var(--white); text-transform: uppercase;
  }
  .contact {
    position: absolute; top: 118px; right: 26px;
    text-align: right; font-size: 10.5px; line-height: 1.55;
  }
  .contact .email { display: flex; align-items: center; justify-content: flex-end; gap: 5px; }
  .contact .web { font-weight: 700; font-size: 13px; }
  .person { position: absolute; top: 148px; left: 30px; }
  .person-name { font-weight: 700; font-size: 17px; letter-spacing: 1px; color: var(--orange); text-transform: uppercase; }
  .person-title { font-size: 11px; color: var(--white); }
  .license { position: absolute; top: 184px; left: 300px; font-size: 9.5px; }
  .locations {
    position: absolute; left: 26px; bottom: 22px;
    font-size: 9.5px; line-height: 1.4; color: var(--ink);
  }
  .phones {
    position: absolute; left: 265px; bottom: 44px;
    display: grid; grid-template-columns: auto auto; column-gap: 18px;
    font-size: 9.5px; font-weight: 600; color: var(--ink); line-height: 1.55;
  }
  .phones span::before { content: "■ "; color: var(--green-deep); font-size: 7px; }
  .certs {
    position: absolute; left: 0; right: 0; bottom: 12px;
    text-align: center; padding-left: 130px;
    font-size: 9.5px; color: var(--ink);
  }
  /* Back */
  .card-back {
    left: 620px;
    background: linear-gradient(180deg, var(--green-pale), var(--green-light));
    color: var(--ink);
  }
  .back-wave { position: absolute; left: 0; bottom: 0; width: 540px; height: 120px; }
  .naics {
    position: absolute; top: 14px; left: 28px;
    list-style: none; font-size: 9.3px; line-height: 1.5; color: var(--ink-soft);
  }
  .back-mark {
    position: absolute; right: 34px; bottom: 28px;
    display: flex; flex-direction: column; align-items: center; gap: 8px;
  }
  .back-mark .brand-dot { width: 96px; height: 96px; }
  .back-mark .brand-name { font-size: 14px; color: var(--ink); letter-spacing: 2px; }
</style>
</head>
<body>

<section class="card card-front">
  <svg class="front-wave" viewBox="0 0 540 160" preserveAspectRatio="none" aria-hidden="true">
    <path d="M0 70 C150 20 330 30 540 60 L540 160 L0 160 Z" fill="var(--green-deep)"/>
    <path d="M0 82 C150 36 330 44 540 72 L540 160 L0 160 Z" fill="var(--green)"/>
    <path d="M0 96 C170 56 340 60 540 86 L540 160 L0 160 Z" fill="var(--green-light)"/>
  </svg>

  <div class="brand">
    <div class="brand-dot"></div>
    <div class="brand-name">Farwell Group</div>
  </div>

  <div class="contact">
    <div class="email">
      <svg width="12" height="9" viewBox="0 0 12 9" aria-hidden="true"><rect x=".5" y=".5" width="11" height="8" fill="none" stroke="#fff"/><path d="M.5 .5 6 5 11.5 .5" fill="none" stroke="#fff"/></svg>
      greta@farwellgrp.net
    </div>
    <div>3620 E Tamsin Road, Orange, CA 92814</div>
    <div class="web">www.farwellgrp.net</div>
  </div>

  <div class="person">
    <div class="person-name">Greta Volsky</div>
    <div class="person-title">President</div>
  </div>

  <div class="license">License no. 482650, K, D74</div>

  <div class="locations">Other locations:<br>San Diego, CA and Reno, NV</div>

  <div class="phones">
    <span>1.800.555.0142</span><span>1.714.555.0187</span>
    <span>1.714.555.0163</span><span>1.714.555.0178</span>
  </div>

  <div class="certs">Certifications: *8(a), *SDB, *SBE, *MBE, *DBE, *CBE</div>
</section>

<section class="card card-back">
  <svg class="back-wave" viewBox="0 0 540 120" preserveAspectRatio="none" aria-hidden="true">
    <path d="M0 40 C180 0 360 10 540 30 L540 120 L0 120 Z" fill="var(--green)" opacity=".35"/>
  </svg>

  <ul class="naics">
    <li>221119 – Other Electric Power Generation</li>
    <li>236210 – Industrial Building Construction</li>
    <li>236220 – Commercial and Institutional Building Construction</li>
    <li>237310 – Highway, Street, and Bridge Construction</li>
    <li>238160 – Roofing Contractors</li>
    <li>238170 – Siding Contractors</li>
    <li>238220 – Plumbing, Heating, and Air-Conditioning Contractors</li>
    <li>238310 – Drywall and Insulation Contractors</li>
    <li>238320 – Painting and Wall Covering Contractors</li>
    <li>238340 – Tile and Terrazzo Contractors</li>
    <li>238350 – Finish Carpentry Contractors</li>
    <li>238390 – Other Building Finishing Contractors</li>
    <li>238910 – Site Preparation Contractors</li>
    <li>238990 – All Other Specialty Trade Contractors</li>
    <li>541350 – Building Inspection Services</li>
    <li>561210 – Facilities Support Services</li>
    <li>561790 – Other Services to Buildings and Dwellings</li>
  </ul>

  <div class="back-mark">
    <div class="brand-dot"></div>
    <div class="brand-name">Farwell Group</div>
  </div>
</section>

</body>
</html>
```